LABEL for Extra Virgin Olive oil

Hi everyone!
I would please like your help with the below project.

We will start importing olive oil from Greece and I would like to create the label for the bottle.
Our goal is to create a label that will really promote the raw quality of the natural product (olive oil).
The olive oil we will import will be very high quality, but we don't want the label to promote a luxury product but more just an exceptional quality natural product that is for the many and comes directly from the producer. Potentially the label can also include images (ex. oils, olive trees, land, sea, sun) but we can evaluate that along the way.
The approximate size of the label will be 60x110 mm
The colors should be earth colors
We can discuss any potential questions as soon as we are in contact.

Thank you all in advance for your time and consideration.

Kind regards, Tobias

```html
<!DOCTYPE html>
<html lang="en">
<head>
<meta charset="utf-8">
<title>Extra Virgin Olive Oil – Label</title>
<link rel="stylesheet" href="https://fonts.googleapis.com/css2?family=Courgette&family=Montserrat:wght@500;600&family=Oswald:wght@500&family=Open+Sans:wght@400&display=swap">
<style>
  :root {
    --backdrop: #6f7213;
    --label-white: #ffffff;
    --panel-dark: #262624;
    --panel-mid: #34342f;
    --gold: #d9b45c;
    --gold-light: #f0d68e;
    --olive-green: #9aa83f;
    --olive-deep: #7f8d2a;
    --script-green: #b3c04d;
    --muted-grey: #a8a59a;
    --volume-tone: #bdb7a3;
  }
  html, body {
    margin: 0;
    padding: 0;
    width: 900px;
    height: 1200px;
    overflow: hidden;
    background: var(--backdrop);
  }
  .canvas {
    position: relative;
    width: 900px;
    height: 1200px;
    background: var(--backdrop);
  }
  .label {
    position: absolute;
    left: 238px;
    top: 150px;
    width: 424px;
    height: 900px;
    background: var(--label-white);
    box-shadow: 0 10px 30px rgba(0,0,0,0.18);
  }
  .label-frame {
    position: absolute;
    inset: 0;
    width: 424px;
    height: 900px;
  }
  .label-content {
    position: absolute;
    inset: 0;
    text-align: center;
    color: var(--muted-grey);
  }
  .rating-stars {
    position: absolute;
    top: 36px;
    left: 112px;
    width: 200px;
    height: 30px;
  }
  .quality-line {
    position: absolute;
    top: 68px;
    left: 0;
    right: 0;
    font-family: "Open Sans", sans-serif;
    font-size: 13px;
    line-height: 15px;
    letter-spacing: 0.5px;
    color: var(--muted-grey);
  }
  .branch-art {
    position: absolute;
    top: 108px;
    left: 160px;
    width: 108px;
    height: 88px;
    border-radius: 40% 50% 45% 50%;
    background: radial-gradient(ellipse at 50% 50%, #7d9a2e 0%, #556b1c 60%, rgba(38,38,36,0) 100%);
  }
  .grade {
    position: absolute;
    top: 228px;
    left: 0;
    right: 0;
    font-family: "Montserrat", sans-serif;
    font-weight: 600;
    font-size: 29px;
    line-height: 36px;
    color: var(--olive-green);
    letter-spacing: 0.5px;
  }
  .product-name {
    position: absolute;
    top: 320px;
    left: 0;
    right: 0;
    font-family: "Courgette", cursive;
    font-size: 92px;
    line-height: 96px;
    color: var(--script-green);
  }
  .natural-badge {
    position: absolute;
    top: 583px;
    left: 145px;
    width: 134px;
    height: 90px;
    background: var(--olive-deep);
    border: 3px solid var(--olive-green);
    box-sizing: border-box;
    color: #ffffff;
    font-family: "Open Sans", sans-serif;
    font-size: 26px;
    line-height: 34px;
    padding-top: 10px;
  }
  .splash-art {
    position: absolute;
    top: 700px;
    left: 150px;
    width: 124px;
    height: 108px;
    border-radius: 50% 50% 45% 45%;
    background: radial-gradient(ellipse at 50% 55%, #a9b93a 0%, #6f8a1c 55%, rgba(38,38,36,0) 100%);
  }
  .volume {
    position: absolute;
    top: 828px;
    left: 0;
    right: 0;
    font-family: "Oswald", sans-serif;
    font-weight: 500;
    font-size: 25px;
    line-height: 30px;
    color: var(--volume-tone);
  }
</style>
</head>
<body>
<div class="canvas">
  <div class="label">
    <svg class="label-frame" viewBox="0 0 424 900" aria-hidden="true">
      <defs>
        <linearGradient id="panelShade" x1="0" y1="0" x2="1" y2="0">
          <stop offset="0" stop-color="var(--panel-dark)"/>
          <stop offset="0.45" stop-color="var(--panel-mid)"/>
          <stop offset="1" stop-color="var(--panel-dark)"/>
        </linearGradient>
        <linearGradient id="goldSheen" x1="0" y1="0" x2="1" y2="0">
          <stop offset="0" stop-color="var(--gold)"/>
          <stop offset="0.5" stop-color="var(--gold-light)"/>
          <stop offset="1" stop-color="var(--gold)"/>
        </linearGradient>
      </defs>
      <path class="panel"
            d="M83 14 H341 A84 84 0 0 0 424 84 V816 A84 84 0 0 0 341 886 H83 A84 84 0 0 0 0 816 V84 A84 84 0 0 0 83 14 Z"
            fill="url(#panelShade)" stroke="url(#goldSheen)" stroke-width="10"/>
    </svg>

    <div class="label-content">
      <svg class="rating-stars" viewBox="0 0 200 30" aria-hidden="true">
        <g fill="var(--gold)">
          <polygon points="20,16 22,21 27,21 23,24 25,29 20,26 15,29 17,24 13,21 18,21"/>
          <polygon points="60,6 62,11 67,11 63,14 65,19 60,16 55,19 57,14 53,11 58,11"/>
          <polygon points="100,2 102,7 107,7 103,10 105,15 100,12 95,15 97,10 93,7 98,7"/>
          <polygon points="140,6 142,11 147,11 143,14 145,19 140,16 135,19 137,14 133,11 138,11"/>
          <polygon points="180,16 182,21 187,21 183,24 185,29 180,26 175,29 177,24 173,21 178,21"/>
        </g>
      </svg>
      <div class="quality-line">PREMIUM<br>QUALITY</div>
      <div class="branch-art" role="img" aria-label="Illustration of an olive branch with green olives"></div>
      <div class="grade">EXTRA<br>VERGIN</div>
      <div class="product-name">olive<br>oil</div>
      <div class="natural-badge">100%<br>Natural</div>
      <div class="splash-art" role="img" aria-label="Illustration of green olives splashing into olive oil"></div>
      <div class="volume">500ML</div>
    </div>
  </div>
</div>
</body>
</html>
```